VOLT - Monitoring Natural Hazards from Space Web Application

KORMEL Sarl is a Luxembourg based Space-Startup that works in the field of Earth Observation. KORMEL is a platform able to extract value-added information from satellite data and is specialized in mapping Natural Disaster (floods, fires etc).

We are now developing a new vertical tool, called VOLT, dedicated to the monitoring of natural hazards in Humanitarian Camps around the world.

The goal of VOLT is to hide to the users' all the complexity of the Satellite Image processing and just provide them the results.

This project require to Design 4 pages of VOLT:
• Public Home Page (Code - V01)
• Dashboard (private Home Page) (Code - V03)
• Monitor (web GIS) (Code - V14)
• Registration Page (Code - V04)

We would like to provide the required time to make a good job.

Target Market(s)

Humanitarian Agencies, Goverments

Coding

Coded - Design and coding required

Number of Pages Required

4 page

Font styles to use
Other font styles liked:
• see the manual attached

Requirements
Must have
• 4 pages. One Home, one form, one dashboard and one web map.
Nice to have
• Please read the attachment with all the detailed instructions

```html
<!DOCTYPE html>
<html lang="en">
<head>
<meta charset="utf-8">
<title>VOLT – Monitoring Natural Hazards</title>
<link rel="stylesheet" href="https://fonts.googleapis.com/css2?family=Jost:wght@400;500;600&family=Space+Mono:wght@700&display=swap">
<style>
:root{
  --teal:#2c5665;
  --gold:#f2c13a;
  --white:#ffffff;
  --ink:#1d1d1d;
  --muted:#4a4a4a;
  --night:#0c0c0d;
  --mist:#dadee2;
}
*{margin:0;padding:0;box-sizing:border-box}
html,body{width:1200px;height:3333px;overflow:hidden}
body{font-family:'Jost',sans-serif;color:var(--ink);background:var(--white);position:relative}
.mono{font-family:'Space Mono',monospace;font-weight:700}

/* hero */
.hero{position:absolute;left:0;top:0;width:1200px;height:678px;overflow:hidden;background:var(--teal)}
.hero-backdrop{position:absolute;inset:0;
  background:
   radial-gradient(circle at 1230px -40px,var(--gold) 0,rgba(242,193,58,.7) 180px,rgba(242,193,58,0) 470px),
   radial-gradient(circle at -60px 700px,#f2f3f7 0,rgba(220,226,234,.7) 160px,rgba(44,86,101,0) 430px),
   var(--teal)}
.play{position:absolute;left:572px;top:558px}
.brand{position:absolute;display:flex;align-items:center;gap:20px;color:var(--white)}
.brand-mark{border:3px solid var(--white);border-radius:50%}
.brand-name{font-weight:400;letter-spacing:.18em}
.nav{position:absolute;left:502px;top:47px;display:flex;gap:38px;font-size:20px;color:var(--white)}
.nav .active{color:var(--gold)}
.btn{position:absolute;top:35px;height:55px;border-radius:28px;display:flex;align-items:center;justify-content:center;gap:6px;font-size:18px;font-weight:500}
.btn-register{left:810px;width:134px;border:2px solid var(--white);color:var(--white)}
.btn-login{left:954px;width:135px;background:var(--white);color:var(--ink)}
.hero-title{position:absolute;left:0;width:1200px;top:128px;text-align:center;color:var(--white);font-size:96px;letter-spacing:.55em;text-indent:.55em;line-height:1}
.hero-sub{position:absolute;left:0;width:1200px;top:264px;text-align:center;color:var(--white);font-size:31px;line-height:42px}

/* welcome */
.sat-visual{position:absolute;left:123px;top:728px;width:458px;height:458px;border-radius:50%;
  background:radial-gradient(circle at 45% 40%,#e6e8ec 0,#b8bec6 45%,#4c5966 80%,#1c2230 100%);border:8px solid #1a1a2a}
.welcome-title{position:absolute;left:666px;top:806px;font-size:44px;color:var(--teal);letter-spacing:.02em}
.welcome-copy{position:absolute;left:666px;top:890px;width:432px;font-size:15.5px;line-height:26.5px;color:var(--muted)}
.welcome-copy p+p{margin-top:27px}

/* pricing */
.pricing{position:absolute;left:0;top:1257px;width:1200px;height:861px;background:linear-gradient(180deg,var(--mist) 0,#eef0f2 60%,#f6f6f8 100%)}
.section-title{position:absolute;left:0;width:1200px;text-align:center;font-size:44px}
.pricing .section-title{top:96px;color:var(--teal)}
.pricing-lead{position:absolute;left:0;width:1200px;top:164px;text-align:center;font-size:16px;line-height:27px;color:var(--muted)}
.plans{position:absolute;left:111px;top:279px;width:978px;height:481px;display:flex;box-shadow:0 10px 40px rgba(0,0,0,.08)}
.plan{flex:1;background:var(--white);text-align:center}
.plan-free{background:linear-gradient(90deg,#fff 70%,#f4f4f4)}
.plan-name{height:85px;line-height:98px;font-size:23px;font-weight:500}
.plan-price{height:63px;line-height:63px;color:var(--white);background:var(--teal);font-size:31px;font-weight:600}
.plan-price small{font-size:18px;font-weight:400}
.plan-standard .plan-price{background:var(--gold)}
.plan-features{list-style:none;padding-top:38px;font-size:17px;line-height:37px;color:var(--muted)}

/* stories */
.stories{position:absolute;left:0;top:2118px;width:1200px;height:733px;overflow:hidden;background:var(--teal)}
.stories-backdrop{position:absolute;inset:0;
  background:
   radial-gradient(circle at 0 733px,rgba(242,193,58,.85) 0,rgba(242,193,58,.35) 180px,rgba(44,86,101,0) 380px),
   radial-gradient(circle at 1200px 0,rgba(240,242,240,.8) 0,rgba(159,176,182,.35) 150px,rgba(44,86,101,0) 330px),
   var(--teal)}
.stories .section-title{top:88px;color:var(--white)}
.frame-back{position:absolute;border:2px solid rgba(255,255,255,.35)}
.story-card{position:absolute;left:279px;top:194px;width:642px;height:446px;border:2px solid rgba(255,255,255,.85);
  background:linear-gradient(160deg,#5e6b45 0,#4f6a52 45%,#3e6470 100%)}
.client-badge{position:absolute;left:54px;top:40px;width:169px;height:76px;background:var(--white);display:flex;align-items:center;justify-content:center;color:#e03a2d;font-size:26px;font-weight:600}
.story-quote{position:absolute;left:54px;top:156px;width:560px;color:var(--white);font-size:21.5px;line-height:31.7px}
.avatar{position:absolute;left:54px;top:336px;width:74px;height:74px;border-radius:50%;background:linear-gradient(160deg,#d9d3cc,#8c8a88)}
.author{position:absolute;left:142px;top:346px;color:var(--white);font-size:19px;font-weight:500;line-height:28px}
.author span{display:block;color:var(--gold);font-weight:400}
.arrow{position:absolute;top:394px}

/* footer */
.footer{position:absolute;left:0;top:2851px;width:1200px;height:482px;color:var(--white);
  background:radial-gradient(ellipse at 620px 200px,#3a3126 0,#1b1814 40%,var(--night) 75%)}
.footer-about{position:absolute;left:111px;top:230px;width:450px;font-size:15px;line-height:28px}
.col-title{position:absolute;top:112px;font-size:20px;font-weight:500}
.quick-links{position:absolute;left:659px;top:166px;list-style:none;font-size:15px;line-height:29px}
.socials{position:absolute;left:874px;top:172px;display:flex;gap:10px}
.socials span{width:46px;height:46px;border:1.5px solid var(--white);border-radius:50%;display:flex;align-items:center;justify-content:center;font-size:10px}
.footer-rule{position:absolute;left:111px;top:376px;width:978px;height:1px;background:rgba(255,255,255,.35)}
.copyright{position:absolute;left:0;width:1200px;top:414px;text-align:center;font-size:15.5px}
</style>
</head>
<body>

<header class="hero">
  <div class="hero-backdrop" role="img" aria-label="Decorative orbit artwork over a teal and gold gradient"></div>
  <svg class="play" width="56" height="56" viewBox="0 0 56 56">
    <circle cx="28" cy="28" r="28" fill="#1e2a2f"/>
    <path d="M21 17 L39 28 L21 39 Z" fill="#fff"/>
  </svg>
  <div class="brand" style="left:111px;top:33px">
    <span class="brand-mark" style="width:56px;height:56px"></span>
    <span class="brand-name" style="font-size:40px">VOLT</span>
  </div>
  <nav class="nav"><span class="active">Home</span><span>Features</span><span>Pricing</span></nav>
  <a class="btn btn-register">
    <svg width="14" height="14" viewBox="0 0 14 14"><path d="M2 12 L3 9 L10 2 L12 4 L5 11 Z" fill="#fff"/></svg>REGISTER</a>
  <a class="btn btn-login">
    <svg width="12" height="14" viewBox="0 0 12 14"><rect x="1" y="6" width="10" height="8" rx="1" fill="#1d1d1d"/><path d="M3 6 V4 a3 3 0 0 1 6 0 V6" stroke="#1d1d1d" stroke-width="2" fill="none"/></svg>LOGIN</a>
  <h1 class="hero-title mono">VOLT</h1>
  <p class="hero-sub">dedicated to the monitoring of natural hazards in<br>Humanitarian Camps around the world</p>
</header>

<section class="welcome">
  <div class="sat-visual" role="img" aria-label="Satellite orbiting above Earth, framed in a circular emblem"></div>
  <h2 class="welcome-title mono">WELCOME TO VOLT</h2>
  <div class="welcome-copy">
    <p>Nemo enim ipsam voluptatem quia voluptas sit aspernatur aut odit aut fugit, sed quia consequuntur magni dolores eos qui ratione voluptatem sequi nesciunt.</p>
    <p>Neque porro quisqua est, qui dolorem ipsum quia dolor sit amet, consect etur isci velit, sed quia non numquam eiusodi tempora incidunt ut labore et dolore magnam aliqua corpo ris suscipit laboriosam, nisi ut aliqu.</p>
  </div>
</section>

<section class="pricing">
  <h2 class="section-title mono">PRICING POLICY</h2>
  <p class="pricing-lead">Subscribe to one of our annual subscription models (starting<br>from as low as 417€/month) and that's all!</p>
  <div class="plans">
    <div class="plan plan-free">
      <div class="plan-name">FREE</div>
      <div class="plan-price">€0.00 <small>/month</small></div>
      <ul class="plan-features"><li>Apps &amp; Platform training</li><li>Training for Developers</li><li>Support &amp; Consultancy</li><li>Host your Data</li></ul>
    </div>
    <div class="plan plan-standard">
      <div class="plan-name">STANDARD</div>
      <div class="plan-price">€700.00 <small>/month</small></div>
      <ul class="plan-features"><li>Apps &amp; Platform training</li><li>Training for Developers</li><li>Support &amp; Consultancy</li><li>Host your Data</li><li>Flood Archive</li><li>Urban Flood Map</li></ul>
    </div>
    <div class="plan plan-pro">
      <div class="plan-name">PROFESSIONAL</div>
      <div class="plan-price">€900.00 <small>/month</small></div>
      <ul class="plan-features"><li>Apps &amp; Platform training</li><li>Training for Developers</li><li>Support &amp; Consultancy</li><li>Host your Data</li><li>Flood Archive</li><li>Urban Flood Map</li><li>White Label</li></ul>
    </div>
  </div>
</section>

<section class="stories">
  <div class="stories-backdrop" role="img" aria-label="Glowing planet horizon in gold and pale light"></div>
  <h2 class="section-title mono">SUCCESS STORIES</h2>
  <div class="frame-back" style="left:204px;top:229px;width:80px;height:359px"></div>
  <div class="frame-back" style="left:916px;top:238px;width:80px;height:359px"></div>
  <article class="story-card">
    <div class="client-badge">Swiftline</div>
    <p class="story-quote">“ Nemo enim ipsam voluptatem quia voluptas sit aspgte rnatur aut odit aut fugit, sed quia consequuntur magnide dolores eos qui ratione voluptatem sequi nesciu ndertue porro quisquam est, qui dolorem ipsum quia dofrtlor sit amet, consec onsequtetur, adipisci velit. ”</p>
    <div class="avatar" role="img" aria-label="Portrait of the client"></div>
    <div class="author">Tomas Ferreira<span>EO Manager</span></div>
  </article>
  <svg class="arrow" style="left:111px" width="16" height="28" viewBox="0 0 16 28"><path d="M13 3 L3 14 L13 25" stroke="#fff" stroke-width="3" fill="none"/></svg>
  <svg class="arrow" style="left:1073px" width="16" height="28" viewBox="0 0 16 28"><path d="M3 3 L13 14 L3 25" stroke="#fff" stroke-width="3" fill="none"/></svg>
</section>

<footer class="footer" role="img" aria-label="Night view of Earth city lights from orbit">
  <div class="brand" style="left:114px;top:94px;gap:38px">
    <span class="brand-mark" style="width:96px;height:96px"></span>
    <span class="brand-name" style="font-size:64px">VOLT</span>
  </div>
  <p class="footer-about">Ut enim ad minima veniam, quis nostrum exercitationem ullam corporis suscipit laboriosam, nisi ut aliquid ex ea commodi con sequatur autem vel eum iure reprehenderit qui in ea voluptate velit esse quam nihil molestiae consequ.</p>
  <h3 class="col-title" style="left:659px">Quick Links</h3>
  <ul class="quick-links"><li>Home</li><li>Features</li><li>Pricing</li><li>Register</li><li>Login</li></ul>
  <h3 class="col-title" style="left:873px">Social Media</h3>
  <div class="socials"><span>Nook</span><span>Peep</span><span>Frame</span><span>Guild</span></div>
  <div class="footer-rule"></div>
  <p class="copyright">Copyright © 2024, Volt. All rights reserved. Privacy Policy</p>
</footer>

</body>
</html>
```